Maple Crest Holdings Inc.
Professional
Simon Oduya
Director
Lot 24 Hibiscus Lane Tremont,
Georgetown, Guyana
simon_d_oduya@mailnest-example.com
www.mchi-example.com
Logo and website

```html
<!DOCTYPE html>
<html lang="en">
<head>
<meta charset="utf-8">
<title>Maple Crest Holdings Inc. – Business Card</title>
<link rel="stylesheet" href="https://fonts.googleapis.com/css2?family=Open+Sans:wght@400;600;700;800&display=swap">
<style>
  :root {
    --backdrop: #e9e4de;
    --navy: #1b2a6b;
    --navy-deep: #121c4d;
    --red: #d8161f;
    --red-deep: #8e0c12;
    --white: #ffffff;
    --ink: #1d1d1f;
    --ink-soft: #3a3a3a;
  }
  html, body {
    margin: 0;
    width: 1200px;
    height: 862px;
    overflow: hidden;
    background: var(--backdrop);
    font-family: "Open Sans", Arial, sans-serif;
  }
  .stage { position: relative; width: 1200px; height: 862px; }
  .card {
    position: absolute;
    overflow: hidden;
    box-shadow: 0 6px 18px rgba(0,0,0,.28);
  }
  .card svg { position: absolute; inset: 0; width: 100%; height: 100%; }
  .card-front { left: 132px; top: 67px; width: 612px; height: 365px; background: var(--navy); }
  .card-back {
    left: 475px; top: 456px; width: 605px; height: 348px;
    background: linear-gradient(90deg, var(--red) 0%, #b51018 55%, var(--red-deep) 100%);
  }
  .brand-name {
    position: absolute;
    margin: 0;
    font-weight: 800;
    line-height: 1.05;
  }
  .card-front .brand-name {
    left: 30px; top: 38px; width: 330px;
    font-size: 30px; color: var(--navy);
  }
  .brand-mark {
    display: inline-block; width: 14px; height: 14px; border-radius: 50%;
    background: var(--red); margin-right: 8px; vertical-align: 4px;
  }
  .person { position: absolute; left: 152px; top: 200px; }
  .person-name { margin: 0; font-size: 27px; font-weight: 600; color: var(--ink); line-height: 1.2; }
  .person-role { margin: 2px 0 0 58px; font-size: 17px; color: var(--ink-soft); }
  .contact {
    position: absolute; right: 16px; top: 236px;
    text-align: right; color: var(--white); font-size: 12px; line-height: 1.45;
  }
  .contact p { margin: 0; }
  .contact .address { margin-bottom: 14px; }
  .card-back .brand-name {
    left: 0; right: 0; top: 130px; text-align: center;
    font-size: 38px; color: var(--white);
  }
  .card-back .brand-mark { background: var(--white); width: 18px; height: 18px; }
  .website {
    position: absolute; left: 0; right: 0; top: 272px; margin: 0;
    text-align: center; color: var(--white); font-size: 15px; font-weight: 700;
  }
</style>
</head>
<body>
<main class="stage">
  <section class="card card-front" aria-label="Business card front">
    <svg viewBox="0 0 612 365" preserveAspectRatio="none" aria-hidden="true">
      <defs>
        <linearGradient id="front-blue" x1="0" y1="0" x2="1" y2="1">
          <stop offset="0" stop-color="#2a3d8f"/>
          <stop offset="1" stop-color="#121c4d"/>
        </linearGradient>
      </defs>
      <rect width="612" height="365" fill="url(#front-blue)"/>
      <path class="front-swoosh" fill="#d8161f"
            d="M0,0 L500,0 C590,55 575,150 465,212 C370,268 270,330 160,365 L0,365 Z"/>
      <path class="front-panel" fill="#ffffff"
            d="M0,0 L470,0 C560,50 545,140 440,200 C340,258 235,325 110,365 L0,365 Z"/>
    </svg>
    <h1 class="brand-name"><span class="brand-mark"></span>Maple Crest Holdings Inc.</h1>
    <div class="person">
      <p class="person-name">Simon Oduya</p>
      <p class="person-role">Director</p>
    </div>
    <div class="contact">
      <p class="address">Lot 24 Hibiscus Lane Tremont,<br>Georgetown, Guyana</p>
      <p>Phone : (592) 555 - 0143</p>
      <p>Cell : (592) 555 - 0178</p>
      <p>Email : simon_d_oduya@mailnest-example.com</p>
    </div>
  </section>

  <section class="card card-back" aria-label="Business card back">
    <h2 class="brand-name"><span class="brand-mark"></span>Maple Crest Holdings Inc.</h2>
    <p class="website">www.mchi-example.com</p>
  </section>
</main>
</body>
</html>
```